Card for invoking rights with police

Our criminal defense law firm is seeking proposals for a design for our card intended for clients to carry with them in their car. Upon being pulled over, they would hand this card to the officer.
Text for the back of the card:
"For Law Enforcement:"
"I will comply with lawful orders but respectfully decline any test or other requests without my attorney. I wish to remain silent, do not consent to searches, and request to speak with my attorney now.
The back of the card should prominently feature the text and the firm logo should be secondary.
Front
Must prominently feature contact info: 425-555-0139. Do not include attorney name, email, phone from the example file. This is intended to be generic for the firm and not tied to an individual lawyer.
Included for design reference: current business card, firm logo.
We intend to use pliqo.example to produce the cards.
Updates
The back of the card should prominently display the text regarding invocation of rights. Please title it "For Law Enforcement".
Target Market(s)
People who have been stopped by police
Contact Information for Business Card
see project description
Look and feel
Each slider illustrates characteristics of the customer's brand and the style your logo design should communicate.

```html
<!DOCTYPE html>
<html lang="en">
<head>
<meta charset="UTF-8">
<title>Harlow Law Firm – Rights Card</title>
<link href="https://fonts.googleapis.com/css2?family=Montserrat:wght@300;400;700&display=swap" rel="stylesheet">
<style>
  :root {
    --backdrop: #d3d3d3;
    --card: #111111;
    --ink: #ffffff;
    --navy: #0e2d4f;
    --silver: #e8ecf0;
  }
  * { margin: 0; padding: 0; box-sizing: border-box; }
  html, body { width: 1029px; height: 1200px; overflow: hidden; }
  body {
    background: var(--backdrop);
    font-family: "Montserrat", Arial, sans-serif;
    color: var(--ink);
    position: relative;
  }
  .card {
    position: absolute;
    left: 134px;
    width: 760px;
    height: 434px;
    background: var(--card);
    box-shadow: 0 6px 14px rgba(0,0,0,0.35);
    overflow: hidden;
  }
  .card--front { top: 110px; }
  .card--back { top: 640px; }
  .band { position: absolute; left: 0; top: 0; width: 760px; height: 434px; }

  .contact {
    position: absolute;
    left: 100px; top: 108px;
    display: flex; align-items: center; gap: 34px;
  }
  .contact__icon { width: 92px; height: 92px; flex: none; }
  .contact__number {
    font-weight: 400;
    font-size: 66px;
    letter-spacing: 1px;
    white-space: nowrap;
  }

  .firm-name {
    position: absolute;
    display: flex; align-items: center; gap: 12px;
    font-weight: 400;
    font-size: 20px;
    letter-spacing: 4px;
    color: var(--ink);
    text-transform: uppercase;
    white-space: nowrap;
  }
  .firm-name__mark { width: 24px; height: 24px; background: var(--ink); flex: none; }
  .card--front .firm-name { left: 48px; top: 326px; }
  .card--back .firm-name { left: 50%; transform: translateX(-50%); top: 362px; }

  .website {
    position: absolute;
    right: 46px; bottom: 26px;
    font-size: 21px;
    font-weight: 400;
    color: var(--ink);
    white-space: nowrap;
  }

  .rights__title {
    position: absolute;
    top: 48px; left: 0; width: 100%;
    text-align: center;
    font-weight: 700;
    font-size: 26px;
    letter-spacing: 0.5px;
    text-transform: uppercase;
  }
  .rights__text {
    position: absolute;
    top: 96px; left: 100px; width: 560px;
    text-align: center;
    font-weight: 400;
    font-size: 22px;
    line-height: 1.45;
  }
</style>
</head>
<body>

<section class="card card--front">
  <svg class="band" viewBox="0 0 760 434">
    <defs>
      <linearGradient id="band-front" x1="0" x2="1" y1="0" y2="0">
        <stop offset="0" stop-color="#0e2d4f"/>
        <stop offset="0.45" stop-color="#2a4a6a"/>
        <stop offset="0.62" stop-color="#f2f4f6"/>
        <stop offset="0.78" stop-color="#3b5878"/>
        <stop offset="1" stop-color="#0e2d4f"/>
      </linearGradient>
    </defs>
    <polygon points="0,262 760,340 760,354 0,276" fill="url(#band-front)"/>
  </svg>

  <div class="contact">
    <svg class="contact__icon" viewBox="0 0 92 92" aria-label="Phone">
      <circle cx="46" cy="46" r="46" fill="#ffffff"/>
      <path d="M30 26c3-2 6-2 7 1l4 8c1 2 0 4-2 5l-3 2c2 6 6 11 12 14l2-3c1-2 3-3 5-2l8 4c3 1 3 4 1 7l-3 3c-3 3-8 3-13 1-12-6-20-15-24-27-1-5 0-9 3-11z" fill="#0e2d4f"/>
      <path d="M54 24c7 3 12 9 13 17M56 15c11 4 18 13 20 26" stroke="#0e2d4f" stroke-width="2.5" fill="none" stroke-linecap="round"/>
    </svg>
    <span class="contact__number">425-555-0139</span>
  </div>

  <div class="firm-name"><span class="firm-name__mark"></span>Harlow Law Firm</div>
  <div class="website">www.harlowlawfirm.example</div>
</section>

<section class="card card--back">
  <svg class="band" viewBox="0 0 760 434">
    <defs>
      <linearGradient id="band-back" x1="0" x2="1" y1="0" y2="0">
        <stop offset="0" stop-color="#0e2d4f"/>
        <stop offset="0.35" stop-color="#2a4a6a"/>
        <stop offset="0.6" stop-color="#f2f4f6"/>
        <stop offset="0.75" stop-color="#3b5878"/>
        <stop offset="1" stop-color="#0e2d4f"/>
      </linearGradient>
    </defs>
    <polygon points="0,324 760,306 760,320 0,338" fill="url(#band-back)"/>
  </svg>

  <h1 class="rights__title">For Law Enforcement</h1>
  <p class="rights__text">I will comply with lawful orders but respectfully decline any test or other requests without my attorney. I wish to remain silent, do not consent to searches, and request to speak with my attorney now.</p>

  <div class="firm-name"><span class="firm-name__mark"></span>Harlow Law Firm</div>
</section>

</body>
</html>
```